Harwick Assurance Partners Ltd needs a business card and logo

We need a logo for documents, invoices etc and a business card to match. We are a health auditing, training and consulting company based in NZ and working in both Australia and NZ. We ensure health organisations meet all their compliance requirements and develop expertise in the health auditing sector. The design should in some way reflect either symbols for quality management in the health sector.

Target Market(s)

Health providers and those wishing to increase their capability in meeting and understanding compliance requirements

Industry/Entity Type

Business

Contact Information for Business Card

Logo plus contact details

Logo Text

Health auditing, consultancy and training

Requirements
Must have
• Name and contact details director: Molly Strand, mstrand@hap-example.co.nz, PO Box 318, Warkworth, NZ, cell +6427391065

```html
<!DOCTYPE html>
<html lang="en">
<head>
<meta charset="utf-8">
<title>Harwick Assurance Partners Ltd — Business Card</title>
<link rel="stylesheet" href="https://fonts.googleapis.com/css2?family=Roboto:wght@400;500;700&display=swap">
<style>
  :root {
    --backdrop: #1e1e1e;
    --card-white: #ffffff;
    --card-black: #000000;
    --brand-red: #ed1c24;
    --brand-green: #6cc24a;
    --ink-dark: #111111;
    --ink-light: #ffffff;
  }
  * { box-sizing: border-box; margin: 0; padding: 0; }
  html, body {
    width: 1200px;
    height: 900px;
    overflow: hidden;
    background: var(--backdrop);
    font-family: "Roboto", Arial, sans-serif;
  }
  .canvas { position: relative; width: 1200px; height: 900px; }

  .card {
    position: absolute;
    left: 307px;
    width: 592px;
    height: 346px;
    border-radius: 18px;
    overflow: hidden;
  }
  .card--front { top: 81px; background: var(--card-white); }
  .card--back  { top: 476px; background: var(--card-black); }

  .band { position: absolute; left: 0; width: 100%; }
  .band--top { top: 0; height: 30px; background: var(--card-black); }
  .band--bottom { bottom: 0; height: 29px; background: var(--brand-red); }

  .brand {
    position: absolute;
    left: 0;
    width: 100%;
    display: flex;
    flex-direction: column;
    align-items: center;
  }
  .card--front .brand { top: 146px; }
  .card--back .brand  { top: 88px; }

  .brand__row { display: flex; align-items: center; gap: 12px; }
  .brand__square { width: 30px; height: 30px; background: var(--brand-red); flex: none; }
  .brand__name {
    font-weight: 700;
    font-size: 25px;
    letter-spacing: 0.3px;
    text-transform: uppercase;
    white-space: nowrap;
  }
  .card--front .brand__name { color: var(--ink-dark); }
  .card--back .brand__name  { color: var(--ink-light); }
  .brand__tagline {
    margin-top: 8px;
    font-size: 9px;
    font-weight: 500;
    letter-spacing: 0.6px;
    color: var(--brand-green);
    text-transform: uppercase;
  }

  .contact {
    position: absolute;
    top: 200px;
    left: 0;
    width: 100%;
    text-align: center;
    color: var(--ink-light);
  }
  .contact__name { font-size: 17px; font-weight: 500; letter-spacing: 0.3px; line-height: 20px; }
  .contact__role { font-size: 12px; font-weight: 500; color: var(--brand-red); line-height: 16px; }
  .contact__lines {
    margin-top: 4px;
    display: flex;
    justify-content: center;
    gap: 10px;
    font-size: 15px;
    line-height: 22px;
  }
  .contact__item { display: flex; align-items: center; gap: 7px; }
  .contact__icon { width: 14px; height: 14px; flex: none; }
  .contact__address { font-size: 15px; line-height: 22px; }
</style>
</head>
<body>
<main class="canvas">

  <section class="card card--front" aria-label="Business card front">
    <div class="band band--top"></div>
    <div class="brand">
      <div class="brand__row">
        <span class="brand__square"></span>
        <span class="brand__name">Harwick Assurance Partners Ltd</span>
      </div>
      <p class="brand__tagline">Health auditing, training and consulting</p>
    </div>
    <div class="band band--bottom"></div>
  </section>

  <section class="card card--back" aria-label="Business card back">
    <div class="brand">
      <div class="brand__row">
        <span class="brand__square"></span>
        <span class="brand__name">Harwick Assurance Partners Ltd</span>
      </div>
      <p class="brand__tagline">Health auditing, training and consulting</p>
    </div>

    <div class="contact">
      <p class="contact__name">MOLLY STRAND</p>
      <p class="contact__role">DIRECTOR</p>
      <div class="contact__lines">
        <span class="contact__item">
          <svg class="contact__icon" viewBox="0 0 14 14" aria-hidden="true">
            <rect width="14" height="14" rx="2" fill="#ed1c24"/>
            <path d="M4 3.2c.4-.3.9-.2 1.1.2l.7 1.3c.2.4.1.8-.2 1l-.5.4c.4.9 1.1 1.6 2 2l.4-.5c.3-.3.7-.4 1-.2l1.3.7c.4.2.5.7.2 1.1l-.5.6c-.4.5-1 .6-1.6.4C5.9 9.5 4.5 8.1 3.8 6.1c-.2-.6 0-1.2.4-1.6z" fill="#000"/>
          </svg>
          +6427391065
        </span>
        <span class="contact__item">
          <svg class="contact__icon" viewBox="0 0 14 14" aria-hidden="true">
            <rect width="14" height="14" rx="2" fill="#ed1c24"/>
            <rect x="3" y="4" width="8" height="6" fill="none" stroke="#000" stroke-width="1.2"/>
            <path d="M3 4.3l4 3 4-3" fill="none" stroke="#000" stroke-width="1.2"/>
          </svg>
          mstrand@hap-example.co.nz
        </span>
      </div>
      <p class="contact__address">PO Box 318, Warkworth, NZ</p>
    </div>
  </section>

</main>
</body>
</html>
```